Health care technology software systems

We have a solid logo. We have company colors that will need to be used as well. We just need a great business card design. We sell to health plans but want to be modern

Target Market(s)

Health technology sector selling into Health Plans

Industry/Entity Type

Health Care Technology

Contact Information for Business Card

Name, title, address, phone number, email

Requirements
Must have
• Use of Parvexa corporate colors - Uploaded w/ our logos

```html
<!DOCTYPE html>
<html lang="en">
<head>
<meta charset="utf-8">
<title>Parvexa Business Card</title>
<link rel="stylesheet" href="https://fonts.googleapis.com/css2?family=Montserrat:wght@400;600;700&display=swap">
<style>
  :root {
    --page-bg: #d6d6d6;
    --card-bg: #3f3f41;
    --brand-blue: #2aa5dd;
    --brand-green: #8cc63f;
    --brand-navy: #3a519b;
    --text-light: #ffffff;
  }
  * { margin: 0; padding: 0; box-sizing: border-box; }
  html, body {
    width: 1200px;
    height: 1200px;
    overflow: hidden;
    background: var(--page-bg);
    font-family: "Montserrat", sans-serif;
  }
  .card {
    position: absolute;
    left: 262px;
    width: 686px;
    height: 391px;
    background: var(--card-bg);
    border-radius: 26px;
    overflow: hidden;
  }
  .card--front { top: 165px; }
  .card--back { top: 653px; }

  .contact {
    position: absolute;
    left: 41px;
    top: 104px;
    color: var(--text-light);
  }
  .contact__name {
    font-weight: 700;
    font-size: 21px;
    color: var(--brand-blue);
    line-height: 1.1;
  }
  .contact__title {
    font-size: 14px;
    color: var(--brand-green);
    margin-top: 2px;
  }
  .contact__address {
    font-size: 14.5px;
    line-height: 19.5px;
    margin-top: 14px;
  }
  .contact__lines {
    list-style: none;
    margin-top: 14px;
    font-size: 14.5px;
    line-height: 19.5px;
  }
  .contact__lines li {
    display: flex;
    align-items: center;
    gap: 9px;
  }
  .contact__lines svg {
    width: 12px;
    height: 12px;
    fill: var(--brand-blue);
    flex: none;
  }

  .brand {
    position: absolute;
    display: flex;
    align-items: center;
    color: var(--text-light);
    font-weight: 400;
    letter-spacing: 1px;
  }
  .brand--front {
    left: 386px;
    top: 160px;
    font-size: 52px;
    gap: 16px;
  }
  .brand--back {
    left: 156px;
    top: 150px;
    font-size: 64px;
    gap: 26px;
  }
  .brand__dot {
    border-radius: 50%;
    background: var(--brand-blue);
    flex: none;
  }
  .brand--front .brand__dot { width: 30px; height: 30px; }
  .brand--back .brand__dot { width: 66px; height: 66px; }
</style>
</head>
<body>
  <section class="card card--front">
    <div class="contact">
      <p class="contact__name">Daniel Reyes</p>
      <p class="contact__title">President</p>
      <p class="contact__address">4120 Harbor View Road<br>Juneau<br>Alaska 99801</p>
      <ul class="contact__lines">
        <li><svg viewBox="0 0 24 24"><path d="M6.6 10.8c1.4 2.8 3.8 5.1 6.6 6.6l2.2-2.2c.3-.3.7-.4 1-.2 1.1.4 2.3.6 3.6.6.6 0 1 .4 1 1V20c0 .6-.4 1-1 1C10.6 21 3 13.4 3 4c0-.6.4-1 1-1h3.5c.6 0 1 .4 1 1 0 1.3.2 2.5.6 3.6.1.3 0 .7-.2 1z"/></svg>555-204-7731</li>
        <li><svg viewBox="0 0 24 24"><path d="M7 1h10c1.1 0 2 .9 2 2v18c0 1.1-.9 2-2 2H7c-1.1 0-2-.9-2-2V3c0-1.1.9-2 2-2zm0 3v14h10V4H7z"/></svg>555-318-6642</li>
        <li><svg viewBox="0 0 24 24"><path d="M2 5h20v14H2V5zm2 2v.5l8 5 8-5V7H4z"/></svg>info@parvexa.com</li>
        <li><svg viewBox="0 0 24 24"><circle cx="12" cy="12" r="10"/></svg>www.parvexa.com</li>
      </ul>
    </div>
    <div class="brand brand--front">
      <span class="brand__dot"></span>
      <span class="brand__name">parvexa</span>
    </div>
  </section>

  <section class="card card--back">
    <div class="brand brand--back">
      <span class="brand__dot"></span>
      <span class="brand__name">parvexa</span>
    </div>
  </section>
</body>
</html>
```